Business IT Services Billboard to attract local small businesses

We are Brivolane, a premier Managed Service Provider (MSP) specializing in comprehensive IT services and VOIP phone solutions exclusively for businesses. Our goal is to create a dynamic and visually engaging billboard advertisement that not only highlights our cutting-edge IT solutions but also emphasizes our state-of-the-art VOIP phone services. This billboard should communicate our commitment to providing innovative, reliable, and holistic technology solutions.
Target Market(s)
small business
Industry/Entity Type
Information Technology
Colors
Designer to choose colors to be used in the design.
Look and feel
Each slider illustrates characteristics of the customer's brand and the style your logo design should communicate.

```html
<!DOCTYPE html>
<html lang="en">
<head>
<meta charset="UTF-8">
<title>Brivolane Billboard</title>
<link rel="stylesheet" href="https://fonts.googleapis.com/css2?family=Open+Sans:wght@600;700;800&display=swap">
<style>
  :root {
    --page-bg: #e9e9ec;
    --board-black: #050607;
    --ink-white: #ffffff;
    --accent-blue: #2f7fd6;
    --pill-blue: #2a78c9;
    --glow-teal: #1e5a62;
    --glow-deep: #0b2429;
  }
  html, body {
    margin: 0;
    padding: 0;
    width: 1200px;
    height: 1200px;
    overflow: hidden;
    background: var(--page-bg);
  }
  .canvas {
    position: relative;
    width: 1200px;
    height: 1200px;
    display: flex;
    align-items: center;
    justify-content: center;
  }
  .billboard {
    position: relative;
    width: 1120px;
    height: 400px;
    background: var(--board-black);
    overflow: hidden;
    font-family: "Open Sans", Arial, sans-serif;
    color: var(--ink-white);
  }
  .visual {
    position: absolute;
    top: 0;
    right: 0;
    width: 600px;
    height: 100%;
    background:
      radial-gradient(ellipse 55% 60% at 55% 45%, var(--glow-teal) 0%, var(--glow-deep) 45%, rgba(5,6,7,0) 80%),
      linear-gradient(90deg, rgba(5,6,7,1) 0%, rgba(11,36,41,0.6) 40%, rgba(11,36,41,0.8) 70%, rgba(5,6,7,0.9) 100%);
  }
  .copy {
    position: absolute;
    left: 60px;
    top: 62px;
    width: 720px;
  }
  .headline {
    margin: 0;
    font-weight: 800;
    font-size: 44px;
    line-height: 1.1;
    letter-spacing: 0.5px;
    text-transform: uppercase;
  }
  .headline .line-one {
    display: block;
    padding-left: 108px;
  }
  .subline {
    margin: 12px 0 0;
    font-weight: 700;
    font-size: 19px;
    letter-spacing: 0.2px;
  }
  .cta-pill {
    display: inline-block;
    margin: 16px 0 0 190px;
    padding: 3px 12px;
    background: var(--pill-blue);
    border-radius: 4px;
    font-weight: 700;
    font-size: 18px;
  }
  .web-address {
    margin: 10px 0 0 110px;
    font-weight: 800;
    font-size: 40px;
    letter-spacing: 0.5px;
  }
  .brand-name {
    position: absolute;
    right: 40px;
    top: 96px;
    margin: 0;
    font-weight: 800;
    font-size: 40px;
    color: var(--accent-blue);
    letter-spacing: 1px;
  }
</style>
</head>
<body>
  <main class="canvas">
    <section class="billboard">
      <div class="visual" role="img" aria-label="Hand in a suit sleeve pointing at a glowing digital network of connected points on a dark teal background"></div>
      <div class="copy">
        <h1 class="headline">
          <span class="line-one">Seamless Technology</span>
          <span>Solutions for Modern Businesses</span>
        </h1>
        <p class="subline">Innovative IT and VOIP Solutions Tailored for Your Business Success</p>
        <span class="cta-pill">Transform Your Tech Today</span>
        <p class="web-address">www.brivolane.com</p>
      </div>
      <p class="brand-name">Brivolane</p>
    </section>
  </main>
</body>
</html>
```